Flyer-Design für Physiotherapie-Praxis
Zielgruppe
Wir sind eine Praxis für Physiotherapie und möchten durch diesen Flyer neue Patienten werben. Der Flyer soll in Arztpraxen ausliegen und dort den Patienten direkt ansprechen und auf uns aufmerksam machen. Es ist auch eine Verknüpfung der Therapie mit einem Training in einem Gesundheitsstudio möglich, da im gleichen Haus das Physio Kraftwerk Eichenstetten beheimatet ist.
Aufgabenstellung
Der Fokus auf unsere Prinzipien (Ganzheitliche Therapie, hohes Maß an Therapiemöglichkeiten, Variation in den therapeutischen Ansätzen durch unterschiedlich fortgebildete Therapeuten, die nach den gleichen Idealen arbeiten)

```html
<!DOCTYPE html>
<html lang="de">
<head>
<meta charset="utf-8">
<title>Flyer – Zentrum für Therapie und Training</title>
<link rel="stylesheet" href="https://fonts.googleapis.com/css2?family=Exo+2:wght@500;600&family=Fira+Sans:wght@400;600&display=swap">
<style>
:root{
  --bg:#ebebeb;
  --blue:#1b8fc9;
  --navy:#1d2a5c;
  --white:#ffffff;
  --grey:#7a7a7a;
  --water:#4fb6de;
  --team:#8fc3e6;
  --gym:#b9b4ad;
}
*{box-sizing:border-box;margin:0;padding:0}
html,body{width:1200px;height:803px;overflow:hidden;background:var(--bg)}
body{position:relative;font-family:"Fira Sans",sans-serif;color:var(--white)}
.sheet{position:absolute;left:347px;width:537px;height:383px;background:var(--white)}
.sheet--outside{top:10px}
.sheet--inside{top:410px}
.panel{position:absolute;top:0;height:100%;overflow:hidden}
.panel--blue{background:var(--blue)}
.panel--white{background:var(--white);color:var(--grey)}
.heading{position:absolute;left:13px;font-family:"Exo 2",sans-serif;font-weight:600;font-size:14px;line-height:18px;letter-spacing:.4px;text-transform:uppercase}
.panel--white .heading{color:var(--blue)}
.text{position:absolute;left:13px;right:10px;font-size:6.4px;line-height:10px}
.text b{font-weight:600}
.label{position:absolute;left:13px;font-family:"Exo 2",sans-serif;font-weight:600;font-size:7.5px;letter-spacing:.4px;text-transform:uppercase}
.panel--white .label{color:var(--grey)}
.panel--blue .label{color:var(--navy)}
.photo{position:absolute}
.photo--pool{left:48px;top:241px;width:148px;height:148px;border-radius:50%;background:radial-gradient(circle at 60% 40%,#e9f4f3 0%,#9fd1e2 40%,var(--water) 70%,#1d7fb0 100%)}
.photo--team{left:0;top:144px;width:172px;height:112px;background:linear-gradient(180deg,#3d4a66 0%,var(--team) 45%,#b8d5ea 100%)}
.photo--gym{left:1px;top:221px;width:162px;height:162px;border-radius:50%;background:linear-gradient(180deg,#ece8e2 0%,var(--gym) 60%,#6b6a6a 100%)}
.caption{position:absolute;left:13px;top:259px;font-size:4.8px;font-style:italic}
.brand{position:absolute;left:0;right:0;top:84px;text-align:center;font-family:"Exo 2",sans-serif;font-weight:600;font-size:10px;line-height:13px;color:var(--navy)}
.brand-mark{display:block;width:34px;height:34px;margin:0 auto 8px;border:1.5px solid var(--navy);border-radius:50%}
.curve{position:absolute;left:0;top:156px;width:183px;height:227px}
.hours{position:absolute;left:13px;top:284px;font-size:6.4px;line-height:10px;border-collapse:collapse}
.hours td{padding:0 6px 0 0}
</style>
</head>
<body>

<section class="sheet sheet--outside">
  <div class="panel panel--blue" style="left:0;width:177px">
    <h2 class="heading" style="top:37px">Vielzahl von<br>Therapiemöglich-<br>keiten</h2>
    <p class="text" style="top:106px">Wir haben eine <b>Vielzahl von Therapiegeräten</b> und Hilfsmitteln zur Verfügung, z.B. eine Kletterwand, Sling Trainer, eine Vibrana-Rüttelplatte, ein Balance-Gestell und ein <b>Bewegungsbad</b>!<br><br>Im 32°C warmen Wasser können sich unsere Patienten besser bewegen. Mit unserem Fachwissen und unserer Erfahrung haben wir uns auf die Behandlung orthopädischer, chirurgischer und neurologischer Patienten spezialisiert.</p>
    <div class="photo photo--pool" role="img" aria-label="Foto: Bewegungsbad mit Handlauf und Pflanzen am Fenster"></div>
  </div>

  <div class="panel panel--white" style="left:177px;width:177px">
    <h2 class="heading" style="top:37px">Kontakt</h2>
    <h3 class="label" style="top:80px">Anfahrt</h3>
    <p class="text" style="top:100px">Zentrum für Therapie und Training<br>Lukas Brenner &amp; Sabine Kolb</p>
    <p class="text" style="top:130px">Lindenweg 27<br>90412 Eichenstetten</p>
    <h3 class="label" style="top:160px">Inhaber</h3>
    <p class="text" style="top:180px">Frau Sabine Kolb</p>
  </div>

  <div class="panel panel--white" style="left:354px;width:183px">
    <div class="brand" style="top:30px">
      <span class="brand-mark"></span>
      Zentrum für Therapie &amp; Training<br>Lukas Brenner &amp; Sabine Kolb<br>Inhaber: Sabine Kolb
    </div>
    <svg class="curve" viewBox="0 0 183 227" preserveAspectRatio="none" aria-hidden="true">
      <path d="M0 10 Q90 -2 183 2 L183 227 L0 227 Z" fill="var(--blue)"/>
    </svg>
    <h2 class="heading" style="top:176px;font-weight:500;font-size:10.5px;line-height:12px;color:var(--white)">Wir sind Therapeuten<br>aus <b style="font-weight:600">Überzeugung</b>!</h2>
    <p class="text" style="top:208px;color:var(--white);line-height:9px">Unsere Praxis gibt es <b>seit 1969</b>. In dieser Zeit konnten wir viel Erfahrung sammeln.<br><br><b>Wir</b> sind ein Team aus älteren und jüngeren Therapeuten, aus Masseuren, med. Bademeistern und Physiotherapeuten. Diese bunte Mischung beinhaltet viel <b>Erfahrung</b> und viel <b>Wissen</b>. Beides wird in regelmäßigen internen Fortbildungen ausgetauscht. So ergänzen wir uns stets gegenseitig.<br><br><b>Wir</b> arbeiten als Team <b>Hand in Hand</b> und schätzen das Fachwissen jedes einzelnen Kollegen.<br><br><b>Wir</b> sind <b>motiviert</b> und mit <b>Freude</b> bei der Arbeit, denn wir wissen, was unsere Patienten mit Hilfe der Physiotherapie erreichen können.</p>
  </div>
</section>

<section class="sheet sheet--inside">
  <div class="panel panel--blue" style="left:0;width:182px">
    <h2 class="heading" style="top:37px">Aktives Gesund-<br>heitstraining</h2>
    <p class="text" style="top:81px">Für gute Fortschritte in der Therapie und die Erhaltung dieser Fortschritte ist der Weg zur sportlichen Aktivität essentiell. Diesen Weg erleichtern wir unseren Patienten durch unser Angebot des Aktiven Gesundheitstrainings.</p>
    <div class="photo photo--team" role="img" aria-label="Gruppenfoto des Praxisteams in hellblauen Poloshirts"></div>
    <p class="caption">Unser erfahrenes Team steht Ihnen immer zur Seite.</p>
    <p class="text" style="top:282px">Zusätzlich zu Ihrem Rezept erhalten unsere neuen Patienten einen zusätzlichen und kostenfreien Beratungstermin im Physio Kraftwerk Eichenstetten. In diesem Termin zeigen wir Ihnen Möglichkeiten, selbst etwas zu Ihrer Gesundung beizutragen.</p>
  </div>

  <div class="panel panel--white" style="left:182px;width:178px">
    <h2 class="heading" style="top:37px">Zirkeltraining</h2>
    <p class="text" style="top:81px">Je nachdem, was Ihnen gerade am effektivsten hilft, trainieren Sie 6 x am Kraft-Ausdauer-Zirkel der Firma Vitaro oder am Flexon-Zirkel.</p>
    <p class="text" style="top:121px">Das Training an diesen Geräten ist einfach, sicher und effektiv. Da das Training maximal 35 Minuten Zeit beansprucht ist Zeitmangel kein Argument mehr.</p>
    <div class="photo photo--gym" role="img" aria-label="Foto: Trainingsraum mit Kraft-Ausdauer-Geräten"></div>
  </div>

  <div class="panel panel--blue" style="left:360px;width:177px">
    <h2 class="heading" style="top:37px">So erreichen<br>Sie uns!</h2>
    <h3 class="label" style="top:79px">Online</h3>
    <p class="text" style="top:94px">Weitere Informationen finden Sie auf unserem Internetauftritt unter <b>www.praxis-brenner.de</b>.</p>
    <h3 class="label" style="top:129px">Telefon, Fax &amp; E-Mail</h3>
    <p class="text" style="top:144px">Telefonisch erreichen Sie uns unter folgender Rufnummer: <b>0911 - 480 2266</b></p>
    <p class="text" style="top:174px">Unser Telefax steht unter der Faxnummer <b>0911 - 480 2267</b> für Sie bereit.</p>
    <p class="text" style="top:204px">Möchten Sie uns per E-Mail kontaktieren, dann schreiben Sie doch gerne an unsere Adresse <b>anmeldung@praxis-brenner.de</b>.</p>
    <h3 class="label" style="top:249px">Öffnungszeiten</h3>
    <p class="text" style="top:264px">Wir sind werktags für Sie da:</p>
    <table class="hours">
      <tr><td>Mo. – Do.</td><td>07:00 – 20:00 Uhr</td></tr>
      <tr><td>Fr.</td><td>07:30 – 19:00 Uhr</td></tr>
      <tr><td>Sa.</td><td>07:30 – 12:00 Uhr</td></tr>
    </table>
  </div>
</section>

</body>
</html>
```